A5, portrait
Theme is science
audience is VIPS, politicians, executives
this is a really important event, we want a very classy invitation
include logo for bloom and grow and lumen but lumen one bigger
images attached
Have attached some styles we like but doesn't need to be these colours. If we can incorporate some colours from our logo would be good but don't make too colourful and childish

You’re invited to the official opening and launch of Lumen, Centre of Discovery. an industry first, pioneering, STEM hub.

Saturday 30th April, 2022

10:00 am – 12:00 pm

42 Calder Lane, Wrenfield

Light canapes provided. Dress code is smart/casual

All guests will be given a guided walk through of Australia’s first dedicated STEM education hub for children aged 3-6.

Invitation only

RSVP: 18 April to marketing@bloomandgrow.edu.au

```html
<!DOCTYPE html>
<html lang="en">
<head>
<meta charset="utf-8">
<title>Lumen Launch Invitation</title>
<link rel="stylesheet" href="https://fonts.googleapis.com/css2?family=Cinzel:wght@500;600&family=Crimson+Pro:ital,wght@0,400;0,700;1,400&display=swap">
<style>
  :root {
    --stage: #e7e5e1;
    --ink-deep: #0b0918;
    --ink-mid: #28224c;
    --ink-violet: #3a3272;
    --copper: #c9692c;
    --copper-soft: #a4522a;
    --accent-rose: rgba(128,72,78,0.75);
    --accent-lilac: rgba(120,110,175,0.45);
    --text-light: #f1eef8;
    --rsvp-band: #ffffff;
    --rsvp-ink: #241f48;
  }
  * { margin: 0; padding: 0; box-sizing: border-box; }
  html, body {
    width: 1200px; height: 900px; overflow: hidden;
    background: var(--stage);
  }
  .invitation {
    position: absolute; left: 304px; top: 30px;
    width: 592px; height: 840px; overflow: hidden;
    background: linear-gradient(160deg, var(--ink-deep) 0%, var(--ink-mid) 40%, var(--ink-mid) 62%, var(--ink-deep) 95%);
    font-family: "Crimson Pro", Georgia, serif;
    color: var(--text-light);
    box-shadow: 0 10px 28px rgba(0,0,0,0.25);
  }
  .accent-pattern { position: absolute; }
  .accent-pattern--top {
    left: 380px; top: 0; width: 212px; height: 261px;
    background: linear-gradient(225deg, var(--accent-rose) 0%, rgba(128,72,78,0.35) 55%, rgba(128,72,78,0) 100%);
    clip-path: polygon(0 0, 100% 0, 100% 100%, 80% 100%, 80% 83%, 60% 83%, 60% 66%, 40% 66%, 40% 50%, 0 50%);
  }
  .accent-pattern--bottom {
    left: 0; top: 571px; width: 282px; height: 196px;
    background: linear-gradient(160deg, var(--accent-lilac) 0%, rgba(120,110,175,0.18) 60%, rgba(120,110,175,0) 100%);
    clip-path: polygon(0 0, 100% 0, 100% 100%, 0 100%);
  }
  .venue-photo {
    position: absolute; left: 0; top: 351px; width: 592px; height: 220px;
    background:
      radial-gradient(ellipse 22% 40% at 50% 52%, rgba(150,140,230,0.85) 0%, rgba(90,80,180,0.4) 60%, rgba(0,0,0,0) 100%),
      linear-gradient(180deg, rgba(10,8,30,0.55) 0%, rgba(0,0,0,0) 35%, rgba(0,0,0,0) 70%, rgba(12,10,30,0.55) 100%),
      linear-gradient(90deg, #4a40a8 0%, #5a52b8 25%, #3f3690 50%, #2e2870 75%, #1f1a4a 100%);
  }
  .frame-line { position: absolute; }
  .frame-line--top { left: 43px; top: 46px; width: 320px; height: 2px; background: linear-gradient(90deg, var(--copper), var(--copper-soft)); }
  .frame-line--left { left: 43px; top: 46px; width: 2px; height: 255px; background: linear-gradient(180deg, var(--copper), rgba(201,105,44,0.2)); }
  .frame-line--right { left: 545px; top: 445px; width: 2px; height: 254px; background: linear-gradient(180deg, rgba(201,105,44,0), var(--copper)); }
  .frame-line--bottom { left: 353px; top: 697px; width: 194px; height: 2px; background: linear-gradient(90deg, rgba(201,105,44,0.4), var(--copper)); }
  .headline {
    position: absolute; left: 78px; top: 68px;
    font-family: "Cinzel", "Times New Roman", serif; font-weight: 600;
    color: var(--copper); font-size: 30px; line-height: 33px; letter-spacing: 0.5px;
  }
  .headline-rule {
    position: absolute; left: 222px; top: 129px; width: 183px; height: 1px;
    background: linear-gradient(90deg, var(--copper), rgba(201,105,44,0));
  }
  .intro {
    position: absolute; left: 78px; top: 146px; width: 360px;
    font-style: italic; font-size: 20px; line-height: 24px;
  }
  .details { position: absolute; left: 181px; top: 244px; list-style: none; }
  .details li { display: flex; align-items: center; height: 29.5px; font-size: 21px; }
  .details svg { width: 17px; height: 17px; margin-right: 24px; fill: var(--text-light); }
  .notes {
    position: absolute; left: 78px; top: 590px; width: 420px;
    font-size: 15px; line-height: 23px;
  }
  .invite-only {
    position: absolute; left: 44px; top: 736px; width: 204px; height: 34px;
    border: 2px solid var(--copper);
    color: var(--copper); font-size: 21px; letter-spacing: 0.3px;
    display: flex; align-items: center; justify-content: center;
  }
  .brand { position: absolute; display: flex; align-items: center; color: var(--text-light); font-weight: 700; }
  .brand--lumen { left: 318px; top: 734px; font-size: 30px; letter-spacing: 1px; }
  .brand--lumen .brand-mark { width: 18px; height: 18px; border-radius: 50%; background: var(--text-light); margin-right: 8px; }
  .brand--bloom { left: 482px; top: 738px; width: 80px; font-size: 15px; line-height: 16px; }
  .brand--bloom .brand-mark { flex: none; width: 12px; height: 12px; background: var(--text-light); margin-right: 6px; }
  .rsvp {
    position: absolute; left: 0; top: 800px; width: 592px; height: 40px;
    background: var(--rsvp-band); color: var(--rsvp-ink);
    font-weight: 700; font-size: 20px;
    display: flex; align-items: center; justify-content: center;
  }
</style>
</head>
<body>
  <article class="invitation">
    <div class="accent-pattern accent-pattern--top" role="img" aria-label="Stepped triangle pattern accent in muted rose"></div>
    <div class="venue-photo" role="img" aria-label="Photo of a glowing plasma ball exhibit on a plinth inside the STEM hub"></div>
    <div class="accent-pattern accent-pattern--bottom" role="img" aria-label="Faint triangle pattern accent in lilac"></div>

    <span class="frame-line frame-line--top"></span>
    <span class="frame-line frame-line--left"></span>
    <span class="frame-line frame-line--right"></span>
    <span class="frame-line frame-line--bottom"></span>

    <h1 class="headline">You’re<br>INVITED</h1>
    <span class="headline-rule"></span>

    <p class="intro">to the official opening and launch of Lumen, Centre of Discovery.&nbsp; An industry first, pioneering, STEM hub.</p>

    <ul class="details">
      <li><svg viewBox="0 0 16 16"><path d="M2 3h12v12H2zM3 6v8h10V6zM4 1h2v3H4zM10 1h2v3h-2zM4 7h2v2H4zM7 7h2v2H7zM10 7h2v2h-2zM4 10h2v2H4zM7 10h2v2H7zM10 10h2v2h-2z" fill-rule="evenodd"/></svg>Saturday 30th April, 2022</li>
      <li><svg viewBox="0 0 16 16"><path d="M8 0a8 8 0 1 0 0 16A8 8 0 0 0 8 0zm.8 3v4.7l3 2-0.9 1.3L7.2 8.5V3z"/></svg>10:00 am – 12:00 pm</li>
      <li><svg viewBox="0 0 16 16"><path d="M8 0a5.5 5.5 0 0 0-5.5 5.5C2.5 10 8 16 8 16s5.5-6 5.5-10.5A5.5 5.5 0 0 0 8 0zm0 3.3a2.2 2.2 0 1 1 0 4.4 2.2 2.2 0 0 1 0-4.4z" fill-rule="evenodd"/></svg>42 Calder Lane, Wrenfield</li>
    </ul>

    <p class="notes">Light canapes provided. Dress code is smart/casual<br>All guests will be given a guided walk through of Australia’s first dedicated STEM education hub for children aged 3-6.</p>

    <div class="invite-only">INVITATION ONLY</div>

    <div class="brand brand--lumen"><span class="brand-mark"></span>Lumen</div>
    <div class="brand brand--bloom"><span class="brand-mark"></span>Bloom &amp; Grow</div>

    <footer class="rsvp">RSVP: 18 April to marketing@bloomandgrow.edu.au</footer>
  </article>
</body>
</html>
```